Corvan Metalworks
Business card and stationary
Corvan Metalworks - Construction
Creative Brief
Modern
Paul Henley
Owner
4726 Birchwood Lane Washington, UT 62915
tgr.corvan@examplemail.net
www.corvanmetalworks.example
A TGR Company
We uploaded the .ai file but we like the finished look of the 2 jpeg files. 1 idea we really like is the black jpg with the chrome logo raised up on the front and on the back of the card all the information....maybe a little color....blue, red, or florescent yellow.

```html
<!DOCTYPE html>
<html lang="en">
<head>
<meta charset="utf-8">
<title>Corvan Metalworks — Stationery Set</title>
<link href="https://fonts.googleapis.com/css2?family=Open+Sans:wght@400;600;700&display=swap" rel="stylesheet">
<style>
  :root{
    --paper:#ffffff;
    --steel-dark:#4f5a62;
    --steel:#6f7b84;
    --chrome:#c9d0d5;
    --rule:#b9c1c6;
    --ink:#3a4147;
    --ink-soft:#7a8288;
    --card-black:#1f2225;
    --shadow:0 2px 8px rgba(0,0,0,.18);
  }
  *{box-sizing:border-box;margin:0;padding:0}
  html,body{width:1200px;height:937px;overflow:hidden;background:var(--paper)}
  body{position:relative;font-family:"Open Sans",Arial,sans-serif;color:var(--ink)}
  .sheet{position:absolute;background:var(--paper);box-shadow:var(--shadow);overflow:hidden}
  .swoosh{position:absolute;left:0;bottom:0;width:100%;display:block}

  .wordmark{display:flex;align-items:center;gap:6px;font-weight:700;color:var(--steel);text-transform:uppercase;letter-spacing:.08em;white-space:nowrap}
  .wordmark .mark-square{display:block;flex:none;background:var(--steel)}

  /* Letterhead */
  .letterhead{left:182px;top:68px;width:388px;height:540px}
  .letterhead .wordmark{position:absolute;left:36px;top:34px;font-size:9px}
  .letterhead .wordmark .mark-square{width:9px;height:9px}
  .contact-block{position:absolute;right:30px;top:30px;text-align:right;font-size:5.5px;line-height:1.6;color:var(--ink-soft)}
  .letter-body{position:absolute;left:36px;top:112px;width:316px;font-size:5.6px;line-height:1.65;color:var(--ink)}
  .letter-body p{margin-bottom:9px}
  .signature{width:40px;height:16px;margin:4px 0;background:linear-gradient(90deg,#d9dde0,#eef0f2);border-radius:2px}
  .letter-foot{font-size:5.6px;line-height:1.6;color:var(--ink-soft)}

  /* Presentation sheet */
  .cover{left:633px;top:38px;width:461px;height:577px}
  .cover .wordmark{position:absolute;left:50%;top:262px;transform:translateX(-50%);font-size:17px;color:var(--steel-dark)}
  .cover .wordmark .mark-square{width:16px;height:16px;background:var(--steel-dark)}

  /* Business cards */
  .card-front{left:51px;top:671px;width:177px;height:88px}
  .card-front .wordmark{position:absolute;left:12px;top:12px;font-size:6px}
  .card-front .wordmark .mark-square{width:6px;height:6px}
  .card-front .card-details{position:absolute;left:12px;top:38px;font-size:4.6px;line-height:1.5;color:var(--ink-soft)}
  .card-back{left:51px;top:772px;width:177px;height:114px;background:var(--card-black)}
  .card-back .wordmark{position:absolute;left:50%;top:50%;transform:translate(-50%,-50%);font-size:8px;color:var(--chrome)}
  .card-back .wordmark .mark-square{width:8px;height:8px;background:var(--chrome)}

  /* Compliment slip */
  .slip{left:261px;top:671px;width:435px;height:210px}
  .slip .wordmark{position:absolute;left:26px;top:24px;font-size:8px}
  .slip .wordmark .mark-square{width:8px;height:8px}

  /* Envelope */
  .envelope{left:739px;top:671px;width:431px;height:215px}
  .envelope-art{position:absolute;left:0;top:0;display:block}
  .envelope .web{position:absolute;left:0;top:20px;width:100%;text-align:center;font-size:8px;letter-spacing:.28em;color:#fff;font-weight:600}
</style>
</head>
<body>

<section class="sheet letterhead">
  <div class="wordmark"><span class="mark-square"></span>Corvan Metalworks</div>
  <div class="contact-block">
    Paul Henley<br>4726 Birchwood Lane<br>Washington, UT 62915<br>tgr.corvan@examplemail.net<br>www.corvanmetalworks.example
  </div>
  <div class="letter-body">
    <p>July 8, 2024</p>
    <p>Jane Carter<br>Project Manager<br>210 Main Street, Ogden, UT</p>
    <p>Dear Client,</p>
    <p>Thank you for choosing our shop for your upcoming steel project. We have reviewed the drawings and prepared a detailed quote covering materials, welding, finishing and delivery to your site.</p>
    <p>Our crew can begin fabrication within two weeks of approval and will keep you updated at each stage of the build.</p>
    <p>Please contact us with any questions or changes. We look forward to working with you and your team on this job.</p>
    <p>Best Regards,</p>
    <div class="signature" role="img" aria-label="Handwritten signature"></div>
    <div class="letter-foot">Paul Henley<br>Owner<br>4726 Birchwood Lane, Washington, UT 62915</div>
  </div>
  <svg class="swoosh" viewBox="0 0 388 60" height="60" preserveAspectRatio="none" aria-hidden="true">
    <defs><linearGradient id="steelA" x1="0" y1="0" x2="1" y2="0"><stop offset="0" stop-color="#56626b"/><stop offset=".5" stop-color="#7d8991"/><stop offset="1" stop-color="#56626b"/></linearGradient></defs>
    <path d="M0 14 Q194 -8 388 14" fill="none" stroke="#b9c1c6" stroke-width="1.2"/>
    <path d="M0 24 Q194 0 388 24 L388 60 L0 60 Z" fill="url(#steelA)"/>
  </svg>
</section>

<section class="sheet cover">
  <div class="wordmark"><span class="mark-square"></span>Corvan Metalworks</div>
  <svg class="swoosh" viewBox="0 0 461 70" height="70" preserveAspectRatio="none" aria-hidden="true">
    <defs><linearGradient id="steelB" x1="0" y1="0" x2="1" y2="0"><stop offset="0" stop-color="#56626b"/><stop offset=".5" stop-color="#7d8991"/><stop offset="1" stop-color="#56626b"/></linearGradient></defs>
    <path d="M0 16 Q230 -10 461 16" fill="none" stroke="#b9c1c6" stroke-width="1.4"/>
    <path d="M0 28 Q230 0 461 28 L461 70 L0 70 Z" fill="url(#steelB)"/>
  </svg>
</section>

<section class="sheet card-front">
  <div class="wordmark"><span class="mark-square"></span>Corvan Metalworks</div>
  <div class="card-details">Paul Henley · Owner<br>Steel Fabrication</div>
  <svg class="swoosh" viewBox="0 0 177 22" height="22" preserveAspectRatio="none" aria-hidden="true">
    <path d="M0 6 Q88 -3 177 6" fill="none" stroke="#b9c1c6" stroke-width="1"/>
    <path d="M0 11 Q88 0 177 11 L177 22 L0 22 Z" fill="#6a767f"/>
  </svg>
</section>

<section class="sheet card-back">
  <div class="wordmark"><span class="mark-square"></span>Corvan Metalworks</div>
</section>

<section class="sheet slip">
  <div class="wordmark"><span class="mark-square"></span>Corvan Metalworks</div>
  <svg class="swoosh" viewBox="0 0 435 46" height="46" preserveAspectRatio="none" aria-hidden="true">
    <defs><linearGradient id="steelC" x1="0" y1="0" x2="1" y2="0"><stop offset="0" stop-color="#56626b"/><stop offset=".5" stop-color="#7d8991"/><stop offset="1" stop-color="#56626b"/></linearGradient></defs>
    <path d="M0 12 Q217 -6 435 12" fill="none" stroke="#b9c1c6" stroke-width="1.2"/>
    <path d="M0 20 Q217 0 435 20 L435 46 L0 46 Z" fill="url(#steelC)"/>
  </svg>
</section>

<section class="sheet envelope">
  <svg class="envelope-art" viewBox="0 0 431 215" width="431" height="215" aria-hidden="true">
    <defs><linearGradient id="steelD" x1="0" y1="0" x2="1" y2="0"><stop offset="0" stop-color="#56626b"/><stop offset=".5" stop-color="#7d8991"/><stop offset="1" stop-color="#56626b"/></linearGradient></defs>
    <path d="M0 0 L431 0 L431 52 Q215 78 0 52 Z" fill="url(#steelD)"/>
    <path d="M0 60 Q215 86 431 60" fill="none" stroke="#b9c1c6" stroke-width="1.2"/>
    <path d="M0 215 L215 110 L431 215" fill="none" stroke="#e3e6e8" stroke-width="1"/>
  </svg>
  <div class="web">www.corvanmetalworks.example</div>
</section>

</body>
</html>
```